Morrow Realty Marketing Brochure

We are looking for a refresh/modern design to use on our marketing brochures...the blue paint brush stroke takes up a lot of space and isn't really speaking to us. Most of the material does not need to be reproduced...we are just looking for a clean template that we can use on all of our brochure pages, and then would like help on page 11 to make these pages look more professional.
Target Market(s)
Real Estate Developers, Small Businesses looking to lease space
Industry/Entity Type
Real Estate Development
Requirements
Nice to have
- Colors complementing the Morrow Logo

```html
<!DOCTYPE html>
<html lang="en">
<head>
<meta charset="utf-8">
<title>Morrow Realty Brochure</title>
<link href="https://fonts.googleapis.com/css2?family=Barlow:wght@400;500;600;700&family=Barlow+Semi+Condensed:wght@500;600;700&display=swap" rel="stylesheet">
<style>
:root{
  --blue:#0b4f98;
  --blue-dark:#083d78;
  --cyan:#1aa3d0;
  --grey:#8d95a8;
  --grey-light:#c9cdd6;
  --ink:#1f2f4a;
  --paper:#ffffff;
  --hex:#e6eaf0;
  --bg-top:#1f5fa3;
  --bg-bottom:#8c9bb6;
}
*{margin:0;padding:0;box-sizing:border-box}
html,body{width:1200px;height:2655px;overflow:hidden}
body{background:linear-gradient(180deg,var(--bg-top) 0%,#4f7fb2 45%,var(--bg-bottom) 100%);font-family:"Barlow",sans-serif;color:var(--ink);position:relative}
.sheet{position:absolute;width:447px;height:317px;background:var(--paper);overflow:hidden;box-shadow:0 3px 8px rgba(0,0,0,.25)}
.spread{position:absolute;left:163px;width:895px;height:317px}
.spread .sheet{top:0}
.spread .left{left:0}
.spread .right{left:448px}
.left::after,.right::after{content:"";position:absolute;top:0;bottom:0;width:30px;pointer-events:none}
.left::after{right:0;background:linear-gradient(90deg,rgba(0,0,0,0),rgba(0,0,0,.14))}
.right::after{left:0;background:linear-gradient(90deg,rgba(0,0,0,.16),rgba(0,0,0,0))}
.photo{position:absolute;left:0;top:0;width:447px;height:203px}
.overlay{position:absolute;left:0;top:0;width:447px;height:317px;pointer-events:none}
.tab{position:absolute;left:15px;top:162px;width:150px;height:141px;background:var(--blue);border-radius:22px 30px 0 22px}
.tab-icon{position:absolute;left:16px;top:18px;width:26px;height:26px}
.tab-rule{position:absolute;left:45px;top:14px;width:1px;height:56px;background:rgba(255,255,255,.45)}
.tab-title{position:absolute;left:52px;top:14px;width:90px;color:#fff;font-family:"Barlow Semi Condensed",sans-serif;font-weight:600;font-size:15px;line-height:15px;text-transform:uppercase;letter-spacing:.3px;padding-bottom:4px;border-bottom:1px solid rgba(255,255,255,.45)}
.tab-title small{display:block;font-size:11px;line-height:12px}
.info{position:absolute;left:173px;top:210px;width:152px;height:93px;background:var(--grey);color:#fff;font-size:7.5px;font-weight:600;padding:24px 0 0 14px;line-height:16px}
.info li{list-style:none}
.info li::before{content:"•";margin-right:4px}
.pnum{position:absolute;left:378px;top:220px;width:38px;height:42px}
.pnum span{position:absolute;inset:0;display:flex;align-items:center;justify-content:center;font-size:17px;color:var(--blue);font-weight:500}
.brand{position:absolute;left:364px;top:279px;display:flex;align-items:center;gap:4px}
.brand i{display:block;width:10px;height:10px;background:var(--blue)}
.brand b{font-weight:500;font-size:12px;color:var(--blue);letter-spacing:.3px}
.plan{position:absolute;background:#f1f2f4;border:1px solid #b9bec7}
.legend{position:absolute;left:15px;top:70px;font-size:7px;line-height:9px;color:var(--blue)}
.legend div{display:flex;align-items:center;gap:6px;margin-bottom:6px}
.legend span{display:inline-block;width:11px;height:11px;border-radius:50%}
.callout{position:absolute;background:var(--cyan);color:#fff;font-size:8px;font-weight:600;padding:5px 12px}
.station{position:absolute;width:60px;height:24px;background:#fff;border-radius:3px}
.cover{left:387px;top:28px}
.cover .name{position:absolute;left:295px;top:32px;display:flex;align-items:center;gap:6px}
.cover .name i{width:20px;height:20px;background:var(--blue);display:block}
.cover .name b{font-weight:500;font-size:21px;color:var(--blue);letter-spacing:.5px}
.cover .tagline{position:absolute;left:315px;top:78px;width:110px;font-size:10.5px;line-height:13px;color:var(--blue)}
.back{left:387px;top:2306px}
.back .addr{position:absolute;left:30px;top:30px;font-size:6.5px;line-height:9px;color:var(--ink)}
.back .addr b{font-weight:700}
.back .name{position:absolute;left:30px;top:72px;display:flex;align-items:center;gap:5px}
.back .name i{width:14px;height:14px;background:var(--blue);display:block}
.back .name b{font-weight:500;font-size:15px;color:var(--blue)}
.back .legal{position:absolute;left:30px;top:104px;width:90px;font-size:5px;line-height:6.5px;color:var(--ink)}
.panel-blue{position:absolute;left:0;top:0;width:447px;height:203px;background:var(--blue)}
.panel-title{position:absolute;top:10px;width:100%;text-align:center;color:#fff;font-family:"Barlow Semi Condensed",sans-serif;font-weight:600;font-size:15px;letter-spacing:.4px}
.perk{position:absolute;color:#fff;font-size:6.5px;white-space:nowrap}
.team{position:absolute;top:55px;width:84px;text-align:center;color:#fff}
.team .who{position:absolute;top:100px;left:0;width:84px;font-size:4.6px;line-height:6.2px}
.team .who b{font-size:5.5px;display:block}
.about{position:absolute;left:15px;top:210px;width:310px;height:93px;background:#eceef2;padding:18px 8px 0 0;font-size:4.8px;line-height:7px;color:var(--ink)}
.about p{margin-bottom:2px}
.pin-label{position:absolute;left:45px;top:170px;width:80px;text-align:center;font-family:"Barlow Semi Condensed",sans-serif;font-weight:700;color:var(--blue);font-size:14px;line-height:15px}
</style>
</head>
<body>

<!-- COVER -->
<section class="sheet cover">
  <svg class="overlay" width="447" height="317">
    <line x1="60" y1="0" x2="170" y2="70" stroke="#0b4f98" stroke-width=".6" opacity=".5"/>
    <line x1="300" y1="215" x2="420" y2="160" stroke="#0b4f98" stroke-width=".6" opacity=".5"/>
    <polygon points="188,60 276,111 276,214 188,265 100,214 100,111" fill="#8d9aa6" role="img" aria-label="Photo of a modern office building entrance with landscaping"/>
    <polygon points="0,317 0,262 90,225 188,317" fill="#c9cdd6"/>
    <polygon points="195,317 320,232 447,262 447,317" fill="#0b4f98"/>
    <polygon points="95,238 180,292 165,317 60,317" fill="#0b4f98"/>
  </svg>
  <div class="name"><i></i><b>MORROW</b></div>
  <p class="tagline">Real estate development, project management and advisory</p>
</section>

<!-- SPREAD 1 -->
<div class="spread" style="top:353px">
  <section class="sheet left">
    <div class="photo" role="img" aria-label="Exterior rendering of a two-storey brick office building on a street corner" style="background:linear-gradient(180deg,#dfe5ec 0%,#d2d9e1 38%,#93614a 38%,#8a5a44 78%,#7d7b78 78%,#6f6d6a 100%)"></div>
    <div style="position:absolute;left:0;top:210px;width:325px;height:93px;background:var(--grey-light)"></div>
    <div class="info"><ul><li>57,856 Gross Square Feet</li><li>19,222 SF Floorplates</li><li>Renovations Planned (2021)</li></ul></div>
    <svg width="120" height="160" style="position:absolute;left:30px;top:140px">
      <path d="M55 0 C86 0 110 24 110 55 C110 90 70 115 55 152 C40 115 0 90 0 55 C0 24 24 0 55 0Z" fill="#0b4f98"/>
      <circle cx="55" cy="55" r="41" fill="#fff"/>
    </svg>
    <div class="pin-label">12<br>NORTH<br>ELM</div>
    <svg class="pnum" viewBox="0 0 38 42"><polygon points="19,1 37,11 37,31 19,41 1,31 1,11" fill="none" stroke="#8fb7d8"/></svg><div class="pnum"><span>1</span></div>
    <div class="brand"><i></i><b>MORROW</b></div>
  </section>
  <section class="sheet right">
    <div class="photo" role="img" aria-label="Regional road map of the metro area with the site marked near the lakefront" style="background:linear-gradient(90deg,#e4e7eb 0%,#dde1e6 78%,#aeb5bf 78%,#a9b1bb 100%)"></div>
    <svg class="overlay"><line x1="312" y1="65" x2="348" y2="47" stroke="#1aa3d0" stroke-width=".8"/><circle cx="312" cy="65" r="3.5" fill="#1aa3d0"/></svg>
    <div class="callout" style="left:348px;top:41px;padding:2px 8px;font-size:6px">SITE</div>
    <div class="tab"><svg class="tab-icon" viewBox="0 0 26 26" fill="none" stroke="#fff" stroke-width="1"><path d="M2 6l7-3 8 3 7-3v17l-7 3-8-3-7 3z M9 3v17 M17 6v17"/></svg><div class="tab-rule"></div><div class="tab-title">Regional<br>Map</div></div>
    <div class="info"><ul><li>12 North Elm Avenue</li><li>Brookfield Park, IL 60190</li></ul></div>
    <svg class="pnum" viewBox="0 0 38 42"><polygon points="19,1 37,11 37,31 19,41 1,31 1,11" fill="none" stroke="#8fb7d8"/></svg><div class="pnum"><span>2</span></div>
    <div class="brand"><i></i><b>MORROW</b></div>
  </section>
</div>

<!-- SPREAD 2 -->
<div class="spread" style="top:679px">
  <section class="sheet left">
    <div class="photo" role="img" aria-label="Satellite map showing highway routes to the site" style="background:linear-gradient(135deg,#56664e 0%,#4a5a44 55%,#5a6553 100%)"></div>
    <svg class="overlay"><path d="M45 20 H165 L180 35 V203" fill="none" stroke="#1aa3d0" stroke-width="2"/><line x1="118" y1="89" x2="180" y2="50" stroke="#fff" stroke-width=".7" stroke-dasharray="2 2"/><circle cx="180" cy="50" r="5" fill="#fff"/><circle cx="180" cy="50" r="3" fill="#1aa3d0"/></svg>
    <div class="callout" style="left:55px;top:78px">LOCATION</div>
    <div class="tab"><svg class="tab-icon" viewBox="0 0 26 26" fill="none" stroke="#fff" stroke-width="1"><path d="M4 24V8 M9 24V4 M14 24V10 M19 24V6"/></svg><div class="tab-rule"></div><div class="tab-title">Highway<br>Access</div></div>
    <div class="info"><ul><li>7 Mins / 3 Miles to I-90</li><li>6 Mins / 2.7 Miles to Highway 53</li></ul></div>
    <svg class="pnum" viewBox="0 0 38 42"><polygon points="19,1 37,11 37,31 19,41 1,31 1,11" fill="none" stroke="#8fb7d8"/></svg><div class="pnum"><span>3</span></div>
    <div class="brand"><i></i><b>MORROW</b></div>
  </section>
  <section class="sheet right">
    <div class="photo" role="img" aria-label="Dusk aerial photo of the neighbourhood with the site highlighted" style="background:linear-gradient(180deg,#2b3c66 0%,#3e4b6e 35%,#5b5f66 35%,#545a56 100%)"></div>
    <svg class="overlay"><path d="M112 75 L128 88 V122" fill="none" stroke="#fff" stroke-width=".7" stroke-dasharray="2 2"/><circle cx="128" cy="122" r="2.5" fill="none" stroke="#fff"/><path d="M274 64 H285 L345 172" fill="none" stroke="#fff" stroke-width=".7" stroke-dasharray="2 2"/><circle cx="345" cy="172" r="3" fill="#1aa3d0"/></svg>
    <div class="station" style="left:52px;top:52px"></div>
    <div class="callout" style="left:208px;top:52px">LOCATION</div>
    <div class="tab"><svg class="tab-icon" viewBox="0 0 26 26"><path d="M13 2a8 8 0 0 1 8 8c0 6-8 14-8 14S5 16 5 10a8 8 0 0 1 8-8z" fill="#fff"/><circle cx="13" cy="10" r="3" fill="#0b4f98"/></svg><div class="tab-rule"></div><div class="tab-title">Location<br>Aerial</div></div>
    <div class="info"><ul><li>12 North Elm Avenue</li><li>Brookfield Park, IL 60190</li></ul></div>
    <svg class="pnum" viewBox="0 0 38 42"><polygon points="19,1 37,11 37,31 19,41 1,31 1,11" fill="none" stroke="#8fb7d8"/></svg><div class="pnum"><span>4</span></div>
    <div class="brand"><i></i><b>MORROW</b></div>
  </section>
</div>

<!-- SPREAD 3 -->
<div class="spread" style="top:1005px">
  <section class="sheet left">
    <div class="photo" role="img" aria-label="Aerial map of nearby restaurants and services with numbered markers" style="width:310px;background:linear-gradient(135deg,#5a6670 0%,#4c5860 100%)"></div>
    <div role="img" aria-label="List of nearby restaurants and services" style="position:absolute;left:310px;top:0;width:137px;height:203px;background:#1f4d86"></div>
    <svg class="overlay"><line x1="98" y1="170" x2="160" y2="128" stroke="#fff" stroke-width=".7" stroke-dasharray="2 2"/><circle cx="98" cy="170" r="4" fill="#fff"/><circle cx="98" cy="170" r="2" fill="#0b4f98"/></svg>
    <div class="station" style="left:118px;top:35px"></div>
    <div class="callout" style="left:160px;top:120px;padding:2px 8px">SITE</div>
    <div class="tab"><svg class="tab-icon" viewBox="0 0 26 26" fill="none" stroke="#fff" stroke-width="1"><circle cx="13" cy="13" r="10"/><path d="M9 6v6a2 2 0 0 0 4 0V6 M11 12v8 M17 6c-2 2-2 6 0 7v7"/></svg><div class="tab-rule"></div><div class="tab-title">Restau-<br>rants<br>&amp; Services</div></div>
    <div class="info"><ul><li>12 North Elm Avenue</li><li>Brookfield Park, IL 60190</li></ul></div>
    <svg class="pnum" viewBox="0 0 38 42"><polygon points="19,1 37,11 37,31 19,41 1,31 1,11" fill="none" stroke="#8fb7d8"/></svg><div class="pnum"><span>5</span></div>
    <div class="brand"><i></i><b>MORROW</b></div>
  </section>
  <section class="sheet right">
    <div class="plan" role="img" aria-label="Lower level floorplan drawing" style="left:115px;top:28px;width:210px;height:168px"></div>
    <div class="tab"><svg class="tab-icon" viewBox="0 0 26 26" fill="none" stroke="#fff" stroke-width="1"><rect x="3" y="3" width="20" height="20"/><path d="M3 13h10 M13 3v20 M13 17h10"/></svg><div class="tab-rule"></div><div class="tab-title"><small>Floorplan,</small>Lower<br>Level</div></div>
    <div class="info"><ul><li>19,222 SF Floorplate</li><li>Suites From 1,338 SF</li></ul></div>
    <svg class="pnum" viewBox="0 0 38 42"><polygon points="19,1 37,11 37,31 19,41 1,31 1,11" fill="none" stroke="#8fb7d8"/></svg><div class="pnum"><span>6</span></div>
    <div class="brand"><i></i><b>MORROW</b></div>
  </section>
</div>

<!-- SPREAD 4 -->
<div class="spread" style="top:1331px">
  <section class="sheet left">
    <div class="plan" role="img" aria-label="First floor floorplan drawing" style="left:120px;top:28px;width:218px;height:168px"></div>
    <div class="tab"><svg class="tab-icon" viewBox="0 0 26 26" fill="none" stroke="#fff" stroke-width="1"><rect x="3" y="3" width="20" height="20"/><path d="M3 13h10 M13 3v20 M13 17h10"/></svg><div class="tab-rule"></div><div class="tab-title"><small>Floorplan,</small>1st Flr</div></div>
    <div class="info"><ul><li>19,222 SF Floorplate</li><li>Suites From 1,338 SF</li></ul></div>
    <svg class="pnum" viewBox="0 0 38 42"><polygon points="19,1 37,11 37,31 19,41 1,31 1,11" fill="none" stroke="#8fb7d8"/></svg><div class="pnum"><span>7</span></div>
    <div class="brand"><i></i><b>MORROW</b></div>
  </section>
  <section class="sheet right">
    <div class="legend">
      <div><span style="background:#8fa3bd"></span>LEASED</div>
      <div style="color:var(--cyan)"><span style="background:#9fd3e4"></span>PENDING<br>LEASE</div>
    </div>
    <div class="plan" role="img" aria-label="Second floor floorplan with leased and pending suites shaded" style="left:130px;top:28px;width:218px;height:168px;background:linear-gradient(180deg,#f1f2f4 0%,#f1f2f4 50%,#a9cfe0 50%,#a9cfe0 100%)"></div>
    <div class="tab"><svg class="tab-icon" viewBox="0 0 26 26" fill="none" stroke="#fff" stroke-width="1"><rect x="3" y="3" width="20" height="20"/><path d="M3 13h10 M13 3v20 M13 17h10"/></svg><div class="tab-rule"></div><div class="tab-title"><small>Floorplan,</small>2nd Flr</div></div>
    <div class="info"><ul><li>19,222 SF Floorplate</li><li>Suites From 1,338 SF</li></ul></div>
    <svg class="pnum" viewBox="0 0 38 42"><polygon points="19,1 37,11 37,31 19,41 1,31 1,11" fill="none" stroke="#8fb7d8"/></svg><div class="pnum"><span>8</span></div>
    <div class="brand"><i></i><b>MORROW</b></div>
  </section>
</div>

<!-- SPREAD 5 -->
<div class="spread" style="top:1657px">
  <section class="sheet left">
    <div class="photo" role="img" aria-label="Interior rendering of an open office with workstations" style="background:linear-gradient(180deg,#dcdcd8 0%,#cfcbc3 50%,#45494f 50%,#3e4248 100%)"></div>
    <div class="tab"><svg class="tab-icon" viewBox="0 0 26 26" fill="none" stroke="#fff" stroke-width="1"><path d="M4 24V6h18v18 M4 12h18 M9 6v18 M17 6v18"/></svg><div class="tab-rule"></div><div class="tab-title">Interior<br>Rendering</div></div>
    <div class="info"><ul><li>19,222 SF Floorplate</li><li>Suites From 1,338 SF</li></ul></div>
    <svg class="pnum" viewBox="0 0 38 42"><polygon points="19,1 37,11 37,31 19,41 1,31 1,11" fill="none" stroke="#8fb7d8"/></svg><div class="pnum"><span>9</span></div>
    <div class="brand"><i></i><b>MORROW</b></div>
  </section>
  <section class="sheet right">
    <div class="photo" role="img" aria-label="Exterior rendering of the brick building from the street corner" style="background:linear-gradient(180deg,#e4e9ee 0%,#d5dbe1 30%,#93614a 30%,#87584a 76%,#7d8070 76%,#6f7466 100%)"></div>
    <div class="tab"><svg class="tab-icon" viewBox="0 0 26 26" fill="none" stroke="#fff" stroke-width="1"><path d="M3 24V10h8V4h12v20z M6 14h3 M6 18h3 M15 8h4 M15 12h4 M15 16h4"/></svg><div class="tab-rule"></div><div class="tab-title">Exterior<br>Rendering</div></div>
    <div class="info"><ul><li>19,222 SF Floorplate</li><li>Suites From 1,338 SF</li></ul></div>
    <svg class="pnum" viewBox="0 0 38 42"><polygon points="19,1 37,11 37,31 19,41 1,31 1,11" fill="none" stroke="#8fb7d8"/></svg><div class="pnum"><span>10</span></div>
    <div class="brand"><i></i><b>MORROW</b></div>
  </section>
</div>

<!-- SPREAD 6 -->
<div class="spread" style="top:1982px">
  <section class="sheet left">
    <div class="panel-blue"></div>
    <div class="panel-title" style="left:60px;width:327px">LOCATION PERKS</div>
    <svg class="overlay" width="447" height="317">
      <path d="M152 20H52a4 4 0 0 0-4 4v190" fill="none" stroke="#8fb7d8" stroke-width=".7" stroke-dasharray="2 2"/>
      <defs><polygon id="hx" points="0,-18 16,-9 16,9 0,18 -16,9 -16,-9"/></defs>
      <g fill="#e6eaf0" stroke="#0b4f98" stroke-width="1.5">
        <use href="#hx" x="218" y="75"/><use href="#hx" x="297" y="75"/>
        <use href="#hx" x="164" y="105"/><use href="#hx" x="200" y="105"/>
        <use href="#hx" x="272" y="105"/><use href="#hx" x="218" y="135"/>
        <use href="#hx" x="297" y="135"/><use href="#hx" x="200" y="165"/>
      </g>
      <use href="#hx" x="236" y="105" fill="#083d78" stroke="#0b4f98" stroke-width="1.5"/>
      <g fill="none" stroke="#0b4f98" stroke-width="1.1" stroke-linecap="round" stroke-linejoin="round">
        <!-- wheelchair -->
        <g transform="translate(218 75)"><circle cx="-1" cy="-9" r="1.6"/><path d="M-1-6v6h6l2 6 M-1-2h5"/><path d="M-4-2a6 6 0 1 0 8 7"/></g>
        <!-- cup -->
        <g transform="translate(297 75)"><path d="M-7-3h11v4a5 5 0 0 1-5 5h-1a5 5 0 0 1-5-5z M4-1h2a2 2 0 0 1 0 4h-2 M-8 8h14 M-3-9c-1 2 1 3 0 5 M1-9c-1 2 1 3 0 5"/></g>
        <!-- bike -->
        <g transform="translate(164 105)"><circle cx="-6" cy="4" r="4"/><circle cx="6" cy="4" r="4"/><path d="M-6 4l4-7h6l2 7 M-2-3l3 7 M2-3h-2 M3-7h2"/><circle cx="3" cy="-9" r="1.2"/></g>
        <!-- coworking people -->
        <g transform="translate(200 105)"><circle cx="0" cy="-6" r="2"/><path d="M-3 2v-3a3 3 0 0 1 6 0v3"/><circle cx="-7" cy="1" r="1.6"/><circle cx="7" cy="1" r="1.6"/><path d="M-10 8v-2a3 3 0 0 1 6 0v2 M4 8v-2a3 3 0 0 1 6 0v2 M-3 8v-2a3 3 0 0 1 6 0v2"/></g>
        <!-- document -->
        <g transform="translate(272 105)"><path d="M-6-9h8l4 4v14h-12z M2-9v4h4 M-3-2h6 M-3 1h6 M-3 4h4"/></g>
        <!-- handshake -->
        <g transform="translate(218 135)"><path d="M-10-2l5-5 4 3 4-3 7 5 M-10-2l7 7a1.5 1.5 0 0 0 2-2 M-5 4l2 2a1.5 1.5 0 0 0 2-2 M-1 4l1 1a1.5 1.5 0 0 0 2-2l-4-4 M10-2l-5 5"/></g>
        <!-- conference table -->
        <g transform="translate(297 135)"><path d="M-8-1h16v4h-16z M-6 3v5 M6 3v5"/><circle cx="-5" cy="-6" r="1.6"/><circle cx="0" cy="-6" r="1.6"/><circle cx="5" cy="-6" r="1.6"/></g>
        <!-- wifi -->
        <g transform="translate(200 165)"><path d="M-9-3a13 13 0 0 1 18 0 M-6 0a9 9 0 0 1 12 0 M-3 3a4.5 4.5 0 0 1 6 0"/><circle cx="0" cy="7" r="1.2" fill="#0b4f98"/></g>
      </g>
      <g fill="none" stroke="#fff" stroke-width="1"><circle cx="236" cy="105" r="7"/><path d="M238.5 101.5h-3a1.8 1.8 0 0 0 0 3.5h1.5a1.8 1.8 0 0 1 0 3.5h-3.5 M236 100v10"/></g>
    </svg>
    <div class="perk" style="left:182px;top:48px">Wheelchair Accessible</div>
    <div class="perk" style="left:125px;top:72px">Community Manager</div>
    <div class="perk" style="left:318px;top:72px">Tenant Amenities</div>
    <div class="perk" style="left:64px;top:102px">Bike Room &amp; Showers</div>
    <div class="perk" style="left:294px;top:102px">Flexible Contracts</div>
    <div class="perk" style="left:160px;top:132px">Coworking</div>
    <div class="perk" style="left:318px;top:132px">Conference Rooms</div>
    <div class="perk" style="left:222px;top:162px">Hi-Speed Wi-Fi</div>
    <div role="img" aria-label="Street-level photo of the brick building row" style="position:absolute;left:0;top:210px;width:325px;height:93px;background:linear-gradient(180deg,#e4e9ee 0%,#d4dae0 28%,#93614a 28%,#87584a 80%,#8a8986 80%,#7b7a77 100%)"></div>
    <svg class="pnum" viewBox="0 0 38 42"><polygon points="19,1 37,11 37,31 19,41 1,31 1,11" fill="none" stroke="#8fb7d8"/></svg><div class="pnum"><span>11</span></div>
    <div class="brand"><i></i><b>MORROW</b></div>
  </section>
  <section class="sheet right">
    <div class="panel-blue"></div>
    <div class="panel-title" style="left:0">MEET THE TEAM</div>
    <div class="team" style="left:62px">
      <svg width="84" height="130" viewBox="0 0 84 130"><polygon points="42,8 80,30 80,98 42,120 4,98 4,30" fill="none" stroke="#fff" stroke-width=".8"/><circle cx="80" cy="98" r="1.5" fill="#fff"/><polygon points="42,14 74,33 74,70 42,89 10,70 10,33" fill="#8b9fb8" role="img" aria-label="Portrait of Dana Whitfield"/></svg>
      <div class="who"><b>DANA WHITFIELD</b>T: 312-555-0148<br>dwhitfield@morrowrealty.example</div>
    </div>
    <div class="team" style="left:178px">
      <svg width="84" height="130" viewBox="0 0 84 130"><polygon points="42,8 80,30 80,98 42,120 4,98 4,30" fill="none" stroke="#fff" stroke-width=".8"/><circle cx="80" cy="98" r="1.5" fill="#fff"/><polygon points="42,14 74,33 74,70 42,89 10,70 10,33" fill="#a59a86" role="img" aria-label="Portrait of Leah Corbin"/></svg>
      <div class="who"><b>LEAH CORBIN</b>T: 312-555-0192<br>lcorbin@morrowrealty.example</div>
    </div>
    <div class="team" style="left:294px">
      <svg width="84" height="130" viewBox="0 0 84 130"><polygon points="42,8 80,30 80,98 42,120 4,98 4,30" fill="none" stroke="#fff" stroke-width=".8"/><circle cx="80" cy="98" r="1.5" fill="#fff"/><polygon points="42,14 74,33 74,70 42,89 10,70 10,33" fill="#9a8b7f" role="img" aria-label="Portrait of Marcus Ellery"/></svg>
      <div class="who"><b>MARCUS ELLERY</b>T: 312-555-0117<br>mellery@morrowrealty.example</div>
    </div>
    <div class="about">
      <p>Morrow Realty is a full-service real estate development, management and advisory company with national experience in the acquisition, development and management of commercial and agricultural properties. Using its individual, professional and proven real estate development experience, Morrow maximizes the financial returns of projects by actively managing the real estate planning, permitting, bidding, financing and construction process.</p>
      <p>For more information, visit <b>www.morrowrealty.example</b>.</p>
    </div>
    <svg class="pnum" viewBox="0 0 38 42"><polygon points="19,1 37,11 37,31 19,41 1,31 1,11" fill="none" stroke="#8fb7d8"/></svg><div class="pnum"><span>12</span></div>
    <div class="brand"><i></i><b>MORROW</b></div>
  </section>
</div>

<!-- BACK COVER -->
<section class="sheet back">
  <svg class="overlay" width="447" height="317">
    <line x1="260" y1="60" x2="330" y2="10" stroke="#0b4f98" stroke-width=".6" opacity=".5"/>
    <line x1="5" y1="170" x2="140" y2="230" stroke="#0b4f98" stroke-width=".6" opacity=".5"/>
    <polygon points="250,60 350,118 350,233 250,290 150,233 150,118" fill="#c4b29d" role="img" aria-label="Photo of a bright window with curtains in an interior room"/>
    <polygon points="0,317 0,285 60,255 120,317" fill="#c9cdd6"/>
    <polygon points="40,317 140,250 260,317" fill="#0b4f98"/>
    <polygon points="260,317 447,230 447,317" fill="#c9cdd6"/>
    <polygon points="300,317 400,262 447,285 447,317" fill="#0b4f98"/>
  </svg>
  <div class="addr"><b>MORROW REALTY</b><br>480 Larch Street, Suite 310<br>Brookfield Park, Illinois 60190</div>
  <div class="name"><i></i><b>MORROW</b></div>
  <p class="legal">©2021 Morrow Realty. All rights reserved. All information contained herein is from sources deemed reliable, however, no representation or warranty is made to the accuracy thereof.</p>
</section>

</body>
</html>
```